Vacation rental Management Software company needs website and logo

We need a logo and new website design to promote our vacation rental management software. We sell the software to property owners and management company. We have existing website www.stayquillo.com at the moment but it is need of upgrading. The goal is make it more professional looking and to put the emphasis on marketing the software.
Html + Css code is needed, the website must have responsive layout.
The logo must be composed by the brand "Stayquillo" and eventually an image related to Vacation Rental Management
The pages that we need are the following:
1) Home Page
- must be highlighted the 2 main categories of customers (Direct Owners and Agencies/Portals)
- there must be a section where we can highlight some products, i.e. the latest or the most relevant
- there must be an introductive text
2) Page for a category of customer (owner or agency/portal)
- based on the page http://www.stayquillo.com/owners/ or http://www.stayquillo.com/agencies/, this page must highlight all the products available for the category selected, but must be more attractive then the existing ones (that have just text)
3) Single product page
- in that page must be explained a single product, a page example is this one: http://www.stayquillo.com/owners/vacation-rental-website.html
4) Portfolio page
5) Contact page, with a contact form style

```html
<!DOCTYPE html>
<html lang="en">
<head>
<meta charset="utf-8">
<title>Stayquillo – Vacation Rental Management Software</title>
<link rel="stylesheet" href="https://fonts.googleapis.com/css2?family=Lato:wght@300;400;700;900&family=Raleway:wght@400;600;800&display=swap">
<style>
:root{
  --red:#b5000c;
  --red-dark:#7d0a0c;
  --ink:#222;
  --text:#666;
  --grey-band:#ececec;
  --field:#ededed;
  --field-active:#a9c6e4;
  --white:#fff;
}
*{box-sizing:border-box;margin:0;padding:0}
html,body{width:1200px;height:2687px;overflow:hidden}
body{font-family:'Lato',sans-serif;color:var(--text);background:var(--white);position:relative}
.wrap{position:absolute;left:161px;width:878px}

/* header */
.site-header{position:absolute;top:0;left:0;width:1200px;height:94px;background:#f7f3f3}
.brand{position:absolute;left:168px;top:16px;display:flex;align-items:center;gap:12px;font-weight:900;font-size:36px;color:var(--red)}
.brand-mark{width:34px;height:34px;border-radius:50%;background:var(--red)}
.top-actions{position:absolute;right:160px;top:14px;display:flex;gap:10px}
.pill{font-size:11px;padding:6px 13px;border-radius:14px;background:#fff;border:1px solid #ddd;color:#444;text-transform:uppercase}
.pill.accent{color:var(--red)}
.lang{width:54px;height:26px;border-radius:14px;background:#fff;border:1px solid #ddd;display:flex;align-items:center;justify-content:center;gap:6px}
.lang i{display:block;width:16px;height:11px;background:#2b4a8c}
.main-nav{position:absolute;right:160px;top:60px;display:flex;gap:18px;font-size:11px;font-weight:700;color:#333;text-transform:uppercase}

/* hero */
.hero{position:absolute;top:94px;left:0;width:1200px;height:493px;background:linear-gradient(120deg,#c4121a 0%,#9d0c10 50%,#6f0a0b 100%)}
.hero-title{position:absolute;left:172px;top:222px;color:#fff;font-family:'Raleway',sans-serif}
.hero-title small{display:block;font-size:25px;font-weight:400;letter-spacing:1px}
.hero-title strong{display:block;font-size:41px;font-weight:800;line-height:1.05}
.hero-arrow{position:absolute;top:232px}
.calendar{position:absolute;left:578px;top:46px;width:456px;color:#fff;font-family:'Raleway',sans-serif}
.cal-head{display:flex;justify-content:space-between;align-items:center;font-size:26px;font-weight:600;letter-spacing:3px;height:46px}
.cal-grid{display:grid;grid-template-columns:repeat(7,1fr);grid-template-rows:34px repeat(5,63px);text-align:center;font-size:22px;margin-top:6px;align-items:center}
.cal-grid .dow{font-size:16px;font-weight:600;align-self:start}
.cal-grid span{line-height:38px}
.cal-grid .muted{opacity:.55}
.cal-grid .mark{border:3px solid var(--red);border-radius:50%;width:52px;height:52px;line-height:46px;margin:0 auto;background:rgba(181,0,12,.35)}
.cal-grid .today{background:var(--red);border:3px solid #fff;border-radius:50%;width:48px;height:48px;line-height:42px;margin:0 auto}

/* audience cards */
.audience{position:absolute;top:587px;left:0;width:1200px;height:282px;background:linear-gradient(#fff,var(--grey-band))}
.card{position:absolute;top:47px;width:428px;height:190px;background:#fff;border-radius:5px;box-shadow:0 2px 6px rgba(0,0,0,.15);overflow:hidden}
.card-art{position:absolute;left:0;top:0;width:150px;height:190px;background:var(--red);clip-path:polygon(0 0,100% 0,62% 100%,0 100%)}
.card-art .spot{position:absolute;left:30px;top:40px;width:80px;height:80px;border-radius:50%;background:#e9e1e1}
.card-body{position:absolute;left:150px;top:20px;right:18px}
.card h3{font-size:21px;font-weight:700;color:var(--ink);margin-bottom:10px}
.card p{font-size:11px;line-height:1.55}
.btn-small{display:inline-block;margin-top:12px;font-size:10px;color:var(--red);padding:6px 10px;background:#fff;border:1px solid #eee;border-radius:3px;box-shadow:0 1px 3px rgba(0,0,0,.1);font-weight:700}

/* intro */
.section-title{font-size:17px;font-weight:700;color:var(--ink);line-height:1.3}
.slash{position:absolute;width:2px;height:80px;background:#ddd;transform:rotate(25deg)}
.intro-title{top:873px}
.intro-lead{position:absolute;left:513px;top:916px;width:526px;font-size:11.5px;line-height:1.6}
.intro-body{top:1018px;font-size:11.5px;line-height:1.6}
.intro-body p{margin-bottom:9px}

.values{top:1250px;display:grid;grid-template-columns:repeat(3,1fr);gap:20px;text-align:center}
.values svg{display:block;margin:0 auto 18px}
.values h4{font-size:19px;font-weight:400;color:var(--ink);margin-bottom:10px}
.values p{font-size:11.5px;line-height:1.6;padding:0 18px}
.plus{width:22px;height:22px;border-radius:50%;background:#eee;margin:12px auto 0;position:relative}
.plus::before,.plus::after{content:"";position:absolute;background:#333;left:6px;top:10px;width:10px;height:2px}
.plus::after{transform:rotate(90deg)}

/* testimonials */
.testimonials{position:absolute;top:1516px;left:0;width:1200px;height:324px;background:linear-gradient(90deg,#3a3a3a,#222 50%,#3c3c3c);text-align:center;color:#ddd}
.testimonials h2{font-size:19px;font-weight:700;color:#fff;margin-top:40px}
.quote-mark{font-family:'Raleway',sans-serif;font-size:56px;color:#fff;line-height:1;height:36px;margin-top:6px}
.testimonials blockquote{width:780px;margin:0 auto;font-size:11.5px;line-height:1.75;font-style:italic}
.avatar{width:52px;height:52px;border-radius:50%;background:#fff;margin:16px auto 8px}
.testimonials cite{font-style:normal;font-size:11px;color:#fff}

/* portfolio */
.portfolio-title{top:1903px}
.portfolio-lead{position:absolute;left:513px;top:1880px;width:526px;font-size:11.5px;line-height:1.6}
.projects{top:1981px;display:grid;grid-template-columns:repeat(3,278px);gap:22px}
.project-shot{height:142px;background:var(--red)}
.project-shot.light{background:#e5e5e5}
.project figcaption{font-size:10.5px;font-weight:700;color:var(--ink);margin-top:16px}
.view-more{position:absolute;left:566px;top:2180px;margin:0}
.rule{position:absolute;left:161px;top:2239px;width:878px;height:1px;background:#e3e3e3}

/* contact */
.contact-title{top:2278px}
.contact-form{position:absolute;left:161px;top:2335px;width:578px;display:grid;grid-template-columns:278px 278px;gap:18px 22px}
.field{height:34px;background:var(--field);font-size:10px;color:#888;padding:12px;text-transform:uppercase}
.field.active{background:var(--field-active);color:#fff}
.field.message{grid-column:1/3;height:126px}
.send{grid-column:1/3;height:36px;background:var(--red);color:#fff;font-size:11px;font-weight:700;text-align:center;line-height:36px;margin-top:-4px}
.contact-info{position:absolute;left:817px;top:2335px;font-size:13px;color:#555}
.contact-info li{list-style:none;display:flex;align-items:flex-start;gap:14px;margin-bottom:18px;line-height:1.4}
.social{display:flex;gap:6px;margin-left:32px}
.social span{width:24px;height:24px;background:#2a6db5}

.site-footer{position:absolute;top:2653px;left:0;width:1200px;height:34px;background:#efefef;text-align:center;font-size:10px;line-height:34px;color:#777}
</style>
</head>
<body>

<header class="site-header">
  <div class="brand"><span class="brand-mark"></span>Stayquillo</div>
  <div class="top-actions">
    <span class="pill accent">Owner Login</span>
    <span class="pill">Register Now</span>
    <span class="lang"><i></i><svg width="8" height="6" viewBox="0 0 8 6"><path d="M0 0h8L4 6z" fill="#888"/></svg></span>
  </div>
  <nav class="main-nav"><span>Home</span><span>Products</span><span>Portfolio</span><span>Owners</span><span>Contact Us</span></nav>
</header>

<section class="hero" role="img" aria-label="Photo of a holiday villa under a warm red overlay">
  <svg class="hero-arrow" style="left:112px" width="20" height="40" viewBox="0 0 20 40"><path d="M18 2 2 20l16 18" stroke="#fff" stroke-width="2" fill="none" opacity=".7"/></svg>
  <svg class="hero-arrow" style="left:1066px" width="20" height="40" viewBox="0 0 20 40"><path d="M2 2l16 18L2 38" stroke="#fff" stroke-width="2" fill="none" opacity=".7"/></svg>
  <h1 class="hero-title"><small>THE RIGHT WAY TO</small><strong>MANAGE<br>RESERVATIONS</strong></h1>
  <div class="calendar">
    <div class="cal-head">
      <svg width="12" height="20" viewBox="0 0 12 20"><path d="M10 2 2 10l8 8" stroke="#fff" stroke-width="2" fill="none"/></svg>
      <span>AUGUST 2014</span>
      <svg width="12" height="20" viewBox="0 0 12 20"><path d="M2 2l8 8-8 8" stroke="#fff" stroke-width="2" fill="none"/></svg>
    </div>
    <div class="cal-grid">
      <span class="dow">Mo</span><span class="dow">Tu</span><span class="dow">We</span><span class="dow">Th</span><span class="dow">Fr</span><span class="dow">Sa</span><span class="dow">Su</span>
      <span class="muted">29</span><span class="muted">30</span><span class="muted">31</span><span>1</span><span>2</span><span>3</span><span>4</span>
      <span>5</span><span>6</span><span>7</span><span>8</span><span>9</span><span>10</span><span>11</span>
      <span>12</span><span>13</span><span>14</span><span>15</span><span>16</span><span>17</span><span class="mark">18</span>
      <span>19</span><span>20</span><span>21</span><span>22</span><span class="today">23</span><span>24</span><span>25</span>
      <span>26</span><span>27</span><span>28</span><span>29</span><span>30</span><span>31</span><span class="muted">1</span>
    </div>
  </div>
</section>

<section class="audience">
  <article class="card" style="left:161px">
    <div class="card-art" role="img" aria-label="Illustration of a property owner beneath a house"><div class="spot"></div></div>
    <div class="card-body">
      <h3>Direct Owners</h3>
      <p>If you want to manage all aspects of your properties, if you want to publish them on the most famous portals, if you want to create websites for your properties, check what we offer!</p>
      <span class="btn-small">VIEW MORE</span>
    </div>
  </article>
  <article class="card" style="left:611px">
    <div class="card-art" role="img" aria-label="Illustration of an agent in front of apartment buildings"><div class="spot"></div></div>
    <div class="card-body">
      <h3>Agencies &amp; Portals</h3>
      <p>Discover how we can help you managing data and reservations for the properties you deal with, all your correspondence, all your affiliates, your web presentation and more!</p>
      <span class="btn-small">VIEW MORE</span>
    </div>
  </article>
</section>

<h2 class="wrap section-title intro-title">Professional Vacation &amp; Villa<br>Rental Management Software</h2>
<span class="slash" style="left:470px;top:878px"></span>
<p class="intro-lead">Stayquillo has the best solutions for managing every aspect of villa and vacation rental homes. Built from the ground up around the industry, it is designed to deal with all the day-to-day operations of booking, managing reservations, customer service, communications with clients and owners and more.</p>

<div class="wrap intro-body">
  <p>Stayquillo software is fully integrated into your website both on the front-end and back-end. We make it easy for you to manage both your website and reservations with a seamless solution. Search Engine Optimization (SEO) has been designed into the software enabling you to manage the SEO internally or externally with a consulting firm.</p>
  <p>The software is the ultimate solution for management agencies, booking offices, reservation centers, groups of owners and associations who want to manage their business, clients and customers in a professional manner.</p>
  <p>If you are looking for an affordable professional solution to manage any number of villa or vacation rental properties, please take a look at our Stayquillo Booking Software. You'll be glad you did!</p>
  <p>Brightlet Ltd recently implemented Stayquillo software on their websites including the Hillside Villas and Coastline Villas rental websites and saw a 150% increase in their conversion rate.</p>
</div>

<div class="wrap values">
  <div>
    <svg width="66" height="66" viewBox="0 0 66 66" fill="none" stroke="#b5000c" stroke-width="3"><circle cx="10" cy="48" r="4"/><circle cx="26" cy="28" r="4"/><circle cx="40" cy="40" r="4"/><circle cx="56" cy="12" r="4"/><path d="M13 45l10-14M29 31l8 7M43 37l11-22"/><circle cx="48" cy="50" r="9"/><path d="M42 44l12 12M54 44 42 56"/></svg>
    <h4>Our Mission</h4>
    <p>Lorem ipsum dolor sit amet, consectetur adipisicing elit, sed do eiusmod tempor incididunt ut labore et dolore magna aliqua.</p>
    <div class="plus"></div>
  </div>
  <div>
    <svg width="66" height="66" viewBox="0 0 66 66" fill="none" stroke="#b5000c" stroke-width="3"><circle cx="33" cy="36" r="26"/><path d="M33 36 44 22M15 36h5M46 36h5M33 16v5M20 23l4 4M46 23l-4 4M22 52h22"/></svg>
    <h4>Our Vision</h4>
    <p>Lorem ipsum dolor sit amet, consectetur adipisicing elit, sed do eiusmod tempor incididunt ut labore et dolore magna aliqua.</p>
    <div class="plus"></div>
  </div>
  <div>
    <svg width="66" height="66" viewBox="0 0 66 66" fill="none" stroke="#b5000c" stroke-width="3"><circle cx="33" cy="33" r="24"/><circle cx="33" cy="33" r="12"/><path d="M33 21v12l8 6M12 12l42 42"/></svg>
    <h4>Our History</h4>
    <p>Lorem ipsum dolor sit amet, consectetur adipisicing elit, sed do eiusmod tempor incididunt ut labore et dolore magna aliqua.</p>
    <div class="plus"></div>
  </div>
</div>

<section class="testimonials" role="img" aria-label="Dimmed photo of a villa patio behind the testimonial">
  <h2>Testimonials</h2>
  <div class="quote-mark">&ldquo;</div>
  <blockquote>"Lorem ipsum dolor sit amet, consectetur adipisicing elit, sed do eiusmod tempor incididunt ut labore et dolore magna aliqua. Ut enim ad minim veniam, quis nostrud exercitation ullamco laboris nisi ut aliquip ex ea commodo consequat. Duis aute irure dolor in reprehenderit in voluptate velit esse cillum dolore eu fugiat nulla pariatur. Excepteur sint occaecat cupidatat non proident, sunt in culpa qui officia deserunt mollit anim id est laborum"</blockquote>
  <div class="avatar"></div>
  <cite>Daniel Marsh</cite>
</section>

<h2 class="wrap section-title portfolio-title">Portfolio</h2>
<span class="slash" style="left:470px;top:1872px"></span>
<p class="portfolio-lead">We created our procedures by following agencies and owners who operates worldwide since many years in the holiday homes, villas, apartments and residences sector. In addition to this, to increase our services, we got close collaborations with the most famous vacation rentals portals.</p>

<div class="wrap projects">
  <figure class="project"><div class="project-shot" role="img" aria-label="Client brand panel"></div><figcaption>Brightlet Ltd, Galway, Ireland</figcaption></figure>
  <figure class="project"><div class="project-shot light" role="img" aria-label="Client brand panel"></div><figcaption>Casolare Srl, Vinci, Italy</figcaption></figure>
  <figure class="project"><div class="project-shot" role="img" aria-label="Client brand panel"></div><figcaption>Landhaus Reisen GmbH, Kassel, Germany</figcaption></figure>
</div>
<span class="btn-small view-more">VIEW MORE</span>
<div class="rule"></div>

<h2 class="wrap section-title contact-title">Get In Touch</h2>
<form class="contact-form">
  <div class="field active">Name</div>
  <div class="field">Email</div>
  <div class="field">Phone</div>
  <div class="field">Subject</div>
  <div class="field message">Message</div>
  <div class="send">SEND MESSAGE</div>
</form>
<ul class="contact-info">
  <li><svg width="18" height="18" viewBox="0 0 24 24"><path d="M6 2l4 4-2 3c1 3 4 6 7 7l3-2 4 4-3 4C10 22 2 14 2 5z" fill="#555"/></svg>+44 5550 123</li>
  <li><svg width="18" height="18" viewBox="0 0 24 24" fill="none" stroke="#555" stroke-width="2"><circle cx="12" cy="12" r="9"/><circle cx="12" cy="12" r="3.5"/></svg>info@stayquillo.com</li>
  <li><svg width="18" height="22" viewBox="0 0 24 30" fill="none" stroke="#555" stroke-width="2.5"><path d="M12 28S3 17 3 11a9 9 0 0 1 18 0c0 6-9 17-9 17z"/><circle cx="12" cy="11" r="3"/></svg><span>Lorem ipsum dolor sit,<br>consectetur adipiscing elit,<br>2345687 NL</span></li>
  <li class="social"><span></span><span style="background:#3ba5e0"></span><span style="background:#1d6fa5"></span></li>
</ul>

<footer class="site-footer">Copyright © 2014 Stayquillo. All Rights Reserved</footer>

</body>
</html>
```